Design a beautiful book cover for my self help book

The Craft of Hush is a book I've written about how I learnt to quite my mind, rid myself of old pain and stand in my intuition. It's one simple practical tool to find you moment and step into your abundance. We need a cover that reflects this amazing concept! The current cover is attached. It's too dark and not in tune with the market. Please search books with similar content and make design similar yet different.

Target Market(s)

People into self help or motivational content. As well as people suffering from depression, stress, anxiety etc.

Industry/Entity Type

Self Help

Requirements
Must have
• A light airy feel of freedom
Nice to have
• Some sort of linage from current cover
Should not have
• Dark, ambiguous,

```html
<!DOCTYPE html>
<html lang="en">
<head>
<meta charset="utf-8">
<title>The Craft of Hush — Book Cover</title>
<link rel="stylesheet" href="https://fonts.googleapis.com/css2?family=Dancing+Script:wght@600&family=Montserrat:wght@400;500;700&display=swap">
<style>
  :root {
    --paper: #ffffff;
    --blush: #f8d1e0;
    --blush-deep: #f5c1d7;
    --rose: #ee4e9b;
    --ink: #111111;
    --skin: #e9c0b4;
    --bloom: #d81e6c;
  }
  html, body {
    margin: 0;
    padding: 0;
    width: 1200px;
    height: 933px;
    overflow: hidden;
    background: var(--paper);
  }
  .cover {
    position: relative;
    width: 1200px;
    height: 933px;
    font-family: "Montserrat", sans-serif;
  }
  .back-panel, .front-panel, .spine {
    position: absolute;
    top: 15px;
    height: 892px;
  }
  .back-panel {
    left: 30px;
    width: 548px;
    background: var(--blush);
  }
  .front-panel {
    left: 629px;
    width: 548px;
    background:
      radial-gradient(circle at 20% 12%, var(--blush-deep) 0, transparent 30%),
      radial-gradient(circle at 85% 45%, var(--blush-deep) 0, transparent 28%),
      radial-gradient(circle at 15% 55%, var(--blush-deep) 0, transparent 22%),
      var(--blush);
  }
  .band {
    position: absolute;
    left: 30px;
    top: 660px;
    width: 1147px;
    height: 170px;
  }
  .spine {
    left: 578px;
    width: 51px;
    background: var(--rose);
  }
  .spine-text {
    position: absolute;
    left: 50%;
    color: var(--paper);
    font-weight: 500;
    font-size: 33px;
    line-height: 1;
    white-space: nowrap;
    transform-origin: left top;
    transform: rotate(90deg) translateY(-50%);
  }
  .spine-title { top: 77px; }
  .spine-author { top: 570px; }
  .blurb {
    position: absolute;
    left: 40px;
    top: 76px;
    width: 490px;
    margin: 0;
    text-align: center;
    color: var(--ink);
    font-size: 19.5px;
    line-height: 25.6px;
  }
  .blurb p { margin: 0 0 25.6px; }
  .website {
    position: absolute;
    left: 45px;
    top: 812px;
    color: var(--rose);
    font-size: 19px;
    font-weight: 500;
  }
  .title {
    position: absolute;
    left: 0;
    top: 0;
    margin: 0;
    color: var(--rose);
    font-family: "Dancing Script", cursive;
    font-weight: 600;
    line-height: 1;
  }
  .title-lead {
    position: absolute;
    left: 91px;
    top: 124px;
    font-size: 74px;
    white-space: nowrap;
  }
  .title-main {
    position: absolute;
    left: 168px;
    top: 190px;
    font-size: 150px;
    white-space: nowrap;
  }
  .cover-photo {
    position: absolute;
    left: 145px;
    top: 353px;
    width: 225px;
    height: 355px;
    border-radius: 45% 45% 18% 18%;
    background:
      radial-gradient(circle at 50% 25%, var(--bloom) 0, var(--bloom) 34%, transparent 36%),
      linear-gradient(180deg, var(--skin), #f0cfc6);
  }
  .author {
    position: absolute;
    left: 0;
    width: 548px;
    top: 809px;
    text-align: center;
    color: var(--rose);
    font-size: 40px;
    font-weight: 700;
  }
</style>
</head>
<body>
<div class="cover">
  <section class="back-panel">
    <div class="blurb">
      <p>Do you think too much? Do you overanalyse past events and worry about<br>the future? Are you stuck in your head instead of living in the here and now?</p>
      <p>I used to live in a hamster wheel of thought. I was in a constant state of expectation, speculation, judgement, self-annihilation, stress, anxiety and depression. It wasn't until I practised The Craft of Hush that I was able to find true freedom. The Craft of Hush is a simple yet powerful tool to help you cut the puppet strings of your internal chatter and release the grip of past traumas. It will help you tame your thoughts and reconnect with your intuition.</p>
      <p>Experience the transformative effect of this life-changing practice and embrace a newfound sense of freedom and self-awareness.</p>
    </div>
    <div class="website">www.maralindell.com</div>
  </section>

  <section class="front-panel">
    <h1 class="title">
      <span class="title-lead">The Craft of</span>
      <span class="title-main">Hush</span>
    </h1>
    <div class="cover-photo" role="img" aria-label="Photograph of two cupped hands gently holding a bright pink gerbera daisy"></div>
    <div class="author">Mara Lindell</div>
  </section>

  <svg class="band" viewBox="0 0 1147 170" preserveAspectRatio="none" aria-hidden="true">
    <path d="M0 35 C120 10 260 20 400 45 C470 58 520 60 560 58 C640 40 760 30 860 35 C980 40 1080 25 1147 20 L1147 105 C1060 100 980 110 860 130 C760 148 640 160 560 150 C470 140 380 120 260 115 C150 112 60 120 0 125 Z" fill="var(--rose)"/>
  </svg>

  <section class="spine">
    <span class="spine-text spine-title">The Craft of Hush</span>
    <span class="spine-text spine-author">Mara Lindell</span>
  </section>
</div>
</body>
</html>
```